Singer Renvika needs a CD cover for a new song "Keep the morning glow"

Hi. My name is Renvika. I need a CD cover for my new song "Keep the morning glow"

I want the cover to be drawn with logos of my name and the song title only this time, so "Renvika" and "Keep the morning glow".

My song can be heard from my website: https://renvika.plomsite.example/

Those logos need to be artistic. And probably very colorful. And the logo "Renvika" is at the center. The logo "Keep morning glow" is around it. The background is also to be artistic and colorful.

jpg file is necessary.

I would appreciate that you would challenge this for me. Thanks.

Renvika

Target Market(s)

Music industry

Colors
fbee3e

Requirements
Must have
• The logos of my name and the song title only this time, so "Renvika" and "Keep the morning glow". The logos need to be original design.
Should not have
• Something not original product, dawn from someone's work

```html
<!DOCTYPE html>
<html lang="en">
<head>
<meta charset="utf-8">
<title>Renvika – Keep the morning glow</title>
<link rel="stylesheet" href="https://fonts.googleapis.com/css2?family=Anton&family=Passion+One:wght@700&display=swap">
<style>
  :root {
    --bg-top: #0d2630;
    --bg-mid: #112033;
    --bg-bottom: #24163a;
    --glow-cyan: #52c8ff;
    --glow-blue: #2f8fe0;
    --glow-violet: #8e6ee0;
    --gold-light: #fbee3e;
    --gold: #e6c15e;
    --gold-deep: #a87a2a;
    --white: #ffffff;
    --navy: #23226a;
  }
  html, body {
    margin: 0;
    padding: 0;
    width: 1200px;
    height: 1200px;
    overflow: hidden;
  }
  .cover {
    position: relative;
    width: 1200px;
    height: 1200px;
    overflow: hidden;
    background:
      radial-gradient(ellipse 55% 40% at 40% 75%, rgba(110, 70, 170, 0.45) 0%, transparent 100%),
      radial-gradient(ellipse 60% 45% at 35% 40%, rgba(40, 120, 200, 0.35) 0%, transparent 100%),
      linear-gradient(180deg, var(--bg-top) 0%, var(--bg-mid) 50%, var(--bg-bottom) 100%);
  }
  .light-burst {
    position: absolute;
    inset: 0;
    width: 1200px;
    height: 1200px;
  }
  .glints {
    position: absolute;
    inset: 0;
    background:
      radial-gradient(circle 14px at 435px 215px, rgba(120, 220, 255, 0.95), transparent),
      radial-gradient(circle 16px at 140px 310px, rgba(120, 220, 255, 0.9), transparent),
      radial-gradient(circle 10px at 282px 232px, rgba(120, 220, 255, 0.85), transparent),
      radial-gradient(circle 10px at 670px 295px, rgba(120, 220, 255, 0.85), transparent),
      radial-gradient(circle 8px at 766px 278px, rgba(120, 220, 255, 0.8), transparent),
      radial-gradient(circle 10px at 105px 440px, rgba(120, 220, 255, 0.85), transparent),
      radial-gradient(circle 16px at 150px 615px, rgba(200, 240, 255, 0.95), transparent),
      radial-gradient(circle 10px at 230px 868px, rgba(230, 230, 255, 0.9), transparent),
      radial-gradient(circle 12px at 500px 892px, rgba(230, 220, 255, 0.9), transparent),
      radial-gradient(circle 12px at 632px 892px, rgba(230, 220, 255, 0.9), transparent),
      radial-gradient(circle 14px at 945px 940px, rgba(120, 220, 255, 0.9), transparent),
      radial-gradient(circle 8px at 870px 880px, rgba(120, 220, 255, 0.7), transparent);
  }
  .artist-name {
    position: absolute;
    left: 0;
    top: 357px;
    width: 1200px;
    margin: 0;
    text-align: center;
    font-family: "Anton", sans-serif;
    font-weight: 400;
    font-size: 264px;
    line-height: 1;
    letter-spacing: 12px;
    text-transform: uppercase;
    background: linear-gradient(100deg, var(--gold-deep) 0%, var(--gold) 18%, var(--gold-light) 40%, var(--gold) 60%, var(--gold-deep) 80%, var(--gold) 100%);
    -webkit-background-clip: text;
    background-clip: text;
    color: transparent;
    filter: drop-shadow(8px 6px 6px rgba(0, 0, 0, 0.55));
  }
  .song-title {
    position: absolute;
    left: 0;
    top: 640px;
    width: 1200px;
    margin: 0;
    text-align: center;
    font-family: "Passion One", sans-serif;
    font-weight: 700;
    font-size: 104px;
    line-height: 1;
    color: var(--white);
    -webkit-text-stroke: 8px var(--navy);
    paint-order: stroke fill;
    transform: rotate(-10deg);
    transform-origin: 50% 50%;
  }
  .ornament {
    position: absolute;
    left: 452px;
    top: 1060px;
    width: 296px;
    height: 68px;
    border-radius: 34px;
    background: radial-gradient(ellipse at 50% 50%, rgba(230, 193, 94, 0.75) 0%, rgba(230, 193, 94, 0) 72%);
  }
</style>
</head>
<body>
  <main class="cover">
    <svg class="light-burst" viewBox="0 0 1200 1200" aria-hidden="true">
      <defs>
        <radialGradient id="burst-core" cx="50%" cy="50%" r="50%">
          <stop offset="0%" stop-color="#ffffff" stop-opacity="0.95"/>
          <stop offset="35%" stop-color="#9fdcff" stop-opacity="0.55"/>
          <stop offset="100%" stop-color="#4fc3ff" stop-opacity="0"/>
        </radialGradient>
        <radialGradient id="violet-haze" cx="50%" cy="50%" r="50%">
          <stop offset="0%" stop-color="#b79cff" stop-opacity="0.55"/>
          <stop offset="100%" stop-color="#8e6ee0" stop-opacity="0"/>
        </radialGradient>
        <linearGradient id="ray-fade" x1="0" y1="0" x2="1" y2="1">
          <stop offset="0%" stop-color="#52c8ff" stop-opacity="0"/>
          <stop offset="50%" stop-color="#e6f7ff" stop-opacity="0.95"/>
          <stop offset="100%" stop-color="#52c8ff" stop-opacity="0"/>
        </linearGradient>
        <filter id="soft" x="-20%" y="-20%" width="140%" height="140%">
          <feGaussianBlur stdDeviation="3"/>
        </filter>
        <filter id="wide" x="-20%" y="-20%" width="140%" height="140%">
          <feGaussianBlur stdDeviation="10"/>
        </filter>
      </defs>
      <ellipse cx="470" cy="720" rx="380" ry="170" fill="url(#violet-haze)"/>
      <ellipse cx="500" cy="470" rx="420" ry="260" fill="#2f8fe0" opacity="0.25" filter="url(#wide)"/>
      <ellipse cx="600" cy="620" rx="480" ry="70" fill="url(#burst-core)"/>
      <ellipse cx="640" cy="640" rx="170" ry="120" fill="url(#burst-core)"/>
      <g stroke="url(#ray-fade)" stroke-linecap="round">
        <line x1="260" y1="220" x2="1060" y2="1060" stroke-width="7" filter="url(#soft)"/>
        <line x1="260" y1="220" x2="1060" y2="1060" stroke-width="2"/>
        <line x1="960" y1="330" x2="330" y2="860" stroke-width="4" filter="url(#soft)"/>
        <line x1="1000" y1="480" x2="240" y2="800" stroke-width="3" opacity="0.7"/>
        <line x1="430" y1="260" x2="760" y2="980" stroke-width="2" opacity="0.6"/>
        <line x1="820" y1="250" x2="500" y2="1000" stroke-width="2" opacity="0.55"/>
        <line x1="120" y1="620" x2="1100" y2="620" stroke-width="3" opacity="0.8" filter="url(#soft)"/>
      </g>
    </svg>
    <div class="glints" role="img" aria-label="Scattered blue and violet sparkles around the title"></div>
    <h1 class="artist-name">Renvika</h1>
    <p class="song-title">Keep the morning glow</p>
    <div class="ornament" role="img" aria-label="Gold scroll flourish ornament"></div>
  </main>
</body>
</html>
```